Erstellung einer ersten Einladungskarte „Safe the Date“
Zielgruppe
Spezialist für temporäres Linienmanagement & Projektmanagement
Als Sozietät für professionelles Interim Management bündelt die Lentawerk AG die fachliche Kompetenz und die langjährige Erfahrung erfolgreicher Führungspersönlichkeiten aus nahezu allen Sektoren der Wirtschaft. Wir unterstützen unsere Kunden bei der Bewältigung temporärer Herausforderungen im Linienmanagement sowie im Management komplexer strategischer Projekte und Programme.
https://www.lentawerk.example/de/home.html
Aufgabenstellung
Siehe angehängtes Briefing und angehängtes CD Manual, das nicht zwingend eingehalten werden muss für diesen Job

```html
<!DOCTYPE html>
<html lang="de">
<head>
<meta charset="utf-8">
<title>Save the Date – Lentawerk AG</title>
<link rel="stylesheet" href="https://fonts.googleapis.com/css2?family=Titillium+Web:wght@400&display=swap">
<style>
  :root {
    --page-bg: #ffffff;
    --card-bg: #f7f7f7;
    --brand-blue: #416b8a;
    --brand-blue-soft: #a9bccb;
    --brand-orange: #e8600f;
    --text-light: #ffffff;
  }
  html, body {
    margin: 0;
    padding: 0;
    width: 1200px;
    height: 1200px;
    overflow: hidden;
    background: var(--page-bg);
  }
  .invitation-card {
    position: absolute;
    left: 54px;
    top: 334px;
    width: 1092px;
    height: 520px;
    background: var(--card-bg);
    overflow: hidden;
    font-family: "Titillium Web", sans-serif;
  }
  .event-date {
    position: absolute;
    left: 0;
    right: 0;
    top: 226px;
    margin: 0;
    text-align: center;
    font-size: 21.5px;
    line-height: 30px;
    font-weight: 400;
    color: var(--brand-blue);
  }
  .reminder-figure {
    position: absolute;
    left: 504px;
    top: 334px;
    width: 226px;
    height: 186px;
    border-radius: 60px 60px 0 0;
    background: linear-gradient(180deg, var(--brand-blue-soft) 0%, var(--brand-blue) 70%);
  }
  .speech-tail {
    position: absolute;
    left: 740px;
    top: 413px;
    width: 27px;
    height: 27px;
  }
  .speech-bubble {
    position: absolute;
    left: 767px;
    top: 334px;
    width: 257px;
    height: 140px;
    background: var(--brand-orange);
    display: flex;
    align-items: center;
    box-sizing: border-box;
    padding: 0 0 8px 29px;
  }
  .speech-bubble__text {
    margin: 0;
    color: var(--text-light);
    font-size: 35.5px;
    font-weight: 400;
    line-height: 1;
    white-space: nowrap;
  }
</style>
</head>
<body>
  <main class="invitation-card">
    <p class="event-date">1. und 2. Dezember 2017</p>

    <div class="reminder-figure" role="img" aria-label="Illustration: Geschäftsmann im Anzug als blaue Silhouette, hebt einen Finger mit orangefarbener Erinnerungsschleife"></div>

    <svg class="speech-tail" viewBox="0 0 27 27" aria-hidden="true">
      <polygon points="0,0 27,0 27,27" fill="var(--brand-orange)"/>
    </svg>
    <div class="speech-bubble">
      <p class="speech-bubble__text">Safe the date!</p>
    </div>
  </main>
</body>
</html>
```